Lumora Works - Design & Marketing Website Re-branding

UPDATE:
We are working on finalizing our color palette but are hoping that the designers will guide us to the right choice of colors by looking at our color inspiration file that we just uploaded and lead us in the right direction.

-----

I am exploring new design inspiration for a re-branding of my website. My current website is old and outdated and I lack the time to design it myself in addition to the fact that I am my own worst client.

I do website design, development and marketing as well as some SEO consulting and business development for small to mid-size companies in a range of industries.

https://lumoraworks.example

I like clean modern designs without cartoon images. The brands I'm going after are looking for a professional look and feel. I need something that shows my many years of being in business that is very professional.

I prefer minimal use of color. Mostly black and white with maybe one or two other colors. I am open to the suggestions by the designer.

Target Market(s)

Small to mid-size companies

Industry/Entity Type

Website Design, SEO and Markeitng

Number of Pages Required

4 page

Font styles to use
Sans Serif

Requirements
Must have
• Must be clean, modern and professional - I am not a huge fan of a lot of color and I'm open to new color suggestions by the designer
Nice to have
• A good balance of whitespace to content and graphics
Should not have
• Please no people illustrations

```html
<!DOCTYPE html>
<html lang="en">
<head>
<meta charset="utf-8">
<title>Lumora Works — Design &amp; Marketing</title>
<link rel="stylesheet" href="https://fonts.googleapis.com/css2?family=Outfit:wght@300;400;500;600&family=Work+Sans:wght@400;500;600&display=swap">
<style>
:root{
  --purple:#a55ff2;
  --purple-soft:#d9c3fb;
  --purple-pale:#dcdcff;
  --ink:#111111;
  --text:#3a3a3a;
  --muted:#6b6b6b;
  --grey-band:#f2f2f2;
  --white:#ffffff;
  --line:#d6d6d6;
}
*{margin:0;padding:0;box-sizing:border-box}
html,body{width:1200px;height:3292px;overflow:hidden;background:var(--white)}
body{position:relative;font-family:"Work Sans",Arial,sans-serif;color:var(--text)}
.abs{position:absolute}
h1,h2,h3,.display{font-family:"Outfit",Arial,sans-serif;font-weight:400;color:var(--ink)}

/* header */
.corner-shape{left:1083px;top:-70px;width:190px;height:190px;border-radius:50%;background:var(--purple-pale)}
.corner-lines{left:1148px;top:40px;width:24px}
.corner-lines span{display:block;height:2px;background:#fff;margin-bottom:6px}
.brand{display:flex;align-items:center;gap:10px;font-family:"Outfit",sans-serif;font-weight:600;font-size:30px;color:var(--ink)}
.brand .dot{width:16px;height:16px;border-radius:50%;background:var(--purple)}
.site-brand{left:125px;top:36px}
.main-nav{left:360px;top:48px;display:flex;gap:44px;font-size:14px;color:var(--ink)}

/* hero */
.hero-title{left:125px;top:196px;width:470px;font-size:46px;line-height:52px}
.hero-sub{left:125px;top:378px;width:300px;font-size:13px;line-height:17px;color:var(--ink)}
.btn-ghost{display:flex;align-items:center;gap:18px;background:var(--grey-band);padding:0 22px;height:34px;font-size:12px;font-weight:600;color:var(--ink)}
.hero-btn{left:125px;top:452px}
.arrow-line{display:inline-block;position:relative;width:40px;height:1.5px;background:var(--ink)}
.arrow-line::after{content:"";position:absolute;right:0;top:-3.5px;width:7px;height:7px;border-top:1.5px solid var(--ink);border-right:1.5px solid var(--ink);transform:rotate(45deg)}
.arrow-line.left::after{left:0;right:auto;transform:rotate(-135deg)}
.hero-photo{left:611px;top:150px;width:464px;height:350px;background:linear-gradient(135deg,#e8e6e4 0%,#b9b0a6 45%,#5d5752 100%)}
.slider-arrows{left:930px;top:546px;display:flex;gap:30px}
.slider-arrows .arrow-line{width:60px}

/* services */
.services{left:0;top:597px;width:1200px;height:528px;background:var(--grey-band)}
.eyebrow{font-size:13px;letter-spacing:1px;color:var(--purple);text-transform:uppercase}
.services .eyebrow{position:absolute;left:0;width:1200px;top:99px;text-align:center}
.services h2{position:absolute;left:0;width:1200px;top:125px;text-align:center;font-size:40px;line-height:48px}
.service-card{top:264px;width:330px;height:172px;border-left:2px solid var(--purple);padding-left:22px}
.service-card svg{display:block;margin-top:8px}
.service-card h3{margin-top:14px;font-size:18px;color:var(--ink)}
.service-card p{margin-top:10px;width:190px;font-size:11.5px;line-height:14px;color:var(--text)}
.find-more{margin-top:14px;display:flex;align-items:center;gap:22px;font-size:11px;letter-spacing:1.5px;color:var(--ink)}

/* about */
.about-photo-main{left:125px;top:1264px;width:250px;height:410px;background:linear-gradient(150deg,#9c5a45 0%,#c9b7a6 45%,#6b8aa8 100%)}
.about-photo-inset{left:311px;top:1450px;width:175px;height:245px;border:8px solid var(--white);box-shadow:0 10px 30px rgba(165,95,242,.25);background:linear-gradient(160deg,#d8d2c8 0%,#a89886 50%,#5a5f6b 100%)}
.video-chip{left:369px;top:1290px;width:178px;height:58px;background:var(--white);display:flex;align-items:center;gap:18px;padding-left:18px;font-size:13px;color:var(--ink);box-shadow:0 6px 20px rgba(0,0,0,.08)}
.about-text{left:611px}
.about-eyebrow{top:1222px}
.about-title{top:1246px;width:460px;font-size:40px;line-height:48px}
.about-copy{width:470px;font-size:13px;line-height:16px;color:var(--text)}
.feature{width:240px}
.feature h3{font-size:18px;margin-left:45px}
.feature p{margin:6px 0 0 45px;font-size:11.5px;line-height:14px;color:var(--text)}
.feature svg{position:absolute;left:0;top:22px}

/* testimonials */
.testimonials{left:0;top:1825px;width:1200px;height:611px;background:var(--purple)}
.testimonials h2{position:absolute;left:125px;top:92px;font-size:40px;color:var(--white);font-weight:300}
.testimonials .lead{position:absolute;left:125px;top:154px;width:950px;font-size:12px;line-height:18px;color:var(--white)}
.quote-card{top:239px;width:303px;height:275px;padding:42px 36px 0;text-align:center}
.quote-card.outline{border:1.5px solid var(--purple-soft)}
.quote-card.filled{background:var(--purple-soft)}
.quote-card h3{font-family:"Work Sans",sans-serif;font-size:15px;font-weight:500}
.quote-card p{margin-top:16px;font-size:12px;line-height:20px}
.quote-card.outline h3,.quote-card.outline p{color:var(--white)}
.quote-card.filled h3,.quote-card.filled p{color:var(--ink)}
.quote-badge{position:absolute;left:50%;bottom:-25px;margin-left:-25px;width:50px;height:50px;border-radius:50%;background:var(--white);display:flex;align-items:center;justify-content:center}

/* call to action */
.cta-title{left:0;top:2524px;width:1200px;text-align:center;font-size:40px;line-height:48px}
.cta-btn{left:533px;top:2712px;display:flex;align-items:center;gap:14px}
.cta-btn .label{background:var(--purple-soft);height:38px;width:148px;display:flex;align-items:center;justify-content:center;font-size:12px;font-weight:600;color:var(--ink)}

/* footer */
.site-footer{left:0;top:2853px;width:1200px;height:439px;background:var(--grey-band)}
.footer-brand{left:125px;top:84px}
.social{left:883px;top:82px;display:flex;gap:12px}
.social span{width:34px;height:34px;border-radius:50%;background:var(--purple)}
.footer-rule{left:125px;top:175px;width:950px;height:1px;background:var(--line)}
.footer-kicker{left:125px;top:238px;font-size:17px;font-weight:600;color:var(--ink);letter-spacing:.5px}
.footer-email{left:125px;top:270px;font-family:"Outfit",sans-serif;font-size:38px;font-weight:500;color:var(--ink)}
.copyright{left:125px;top:353px;font-size:13px;color:var(--ink)}
.copyright b{font-weight:600}
.footer-links{top:216px;list-style:none;font-size:14px;color:var(--ink);line-height:40px}
</style>
</head>
<body>

<header>
  <div class="abs corner-shape"></div>
  <div class="abs corner-lines"><span></span><span></span></div>
  <div class="abs brand site-brand"><span class="dot"></span>Lumora Works</div>
  <nav class="abs main-nav"><span>Home</span><span>About Us</span><span>Services</span><span>Blogs</span><span>Contact</span></nav>
</header>

<section class="hero">
  <h1 class="abs hero-title">Every Business Has A Story. We Help You Tell It.</h1>
  <p class="abs hero-sub">Compelling website experiences that elevate your business.</p>
  <div class="abs btn-ghost hero-btn">What We Do <span class="arrow-line"></span></div>
  <div class="abs hero-photo" role="img" aria-label="Photo of a team collaborating around a laptop in an office"></div>
  <div class="abs slider-arrows"><span class="arrow-line left"></span><span class="arrow-line"></span></div>
</section>

<section class="abs services">
  <p class="eyebrow">What We're Offering</p>
  <h2>Services We're Providing<br>To Our Customers</h2>

  <article class="abs service-card" style="left:125px">
    <svg width="46" height="42" viewBox="0 0 46 42" fill="none" stroke="#a55ff2" stroke-width="1.6"><circle cx="23" cy="8" r="5"/><circle cx="8" cy="21" r="5"/><circle cx="38" cy="21" r="5"/><circle cx="23" cy="34" r="5"/><path d="M19 11 12 17M27 11l7 6M12 25l7 6M34 25l-7 6"/></svg>
    <h3>Websites Simplified</h3>
    <p>A complete end-to-end website subscription solution that propels your business forward.</p>
    <div class="find-more">FIND OUT MORE <span class="arrow-line"></span></div>
  </article>
  <article class="abs service-card" style="left:486px">
    <svg width="46" height="42" viewBox="0 0 46 42" fill="none" stroke="#a55ff2" stroke-width="1.6"><rect x="4" y="4" width="38" height="26" rx="2"/><path d="M16 38h14M23 30v8M10 12h14M10 18h20M10 24h10"/></svg>
    <h3>Custom Website Design</h3>
    <p>A complete end-to-end website subscription solution that propels your business forward.</p>
    <div class="find-more">FIND OUT MORE <span class="arrow-line"></span></div>
  </article>
  <article class="abs service-card" style="left:850px">
    <svg width="46" height="42" viewBox="0 0 46 42" fill="none" stroke="#a55ff2" stroke-width="1.6"><circle cx="23" cy="19" r="8"/><circle cx="23" cy="19" r="3"/><path d="M23 5v4M23 29v4M9 19h4M33 19h4M13 9l3 3M30 26l3 3M33 9l-3 3M16 26l-3 3M8 38h30"/></svg>
    <h3>Websites Simplified</h3>
    <p>A complete end-to-end website subscription solution that propels your business forward.</p>
    <div class="find-more">FIND OUT MORE <span class="arrow-line"></span></div>
  </article>
</section>

<section class="about">
  <div class="abs about-photo-main" role="img" aria-label="Photo of smiling colleagues gathered at a desk"></div>
  <div class="abs about-photo-inset" role="img" aria-label="Photo of a team reviewing documents together"></div>
  <div class="abs video-chip">
    <svg width="22" height="22" viewBox="0 0 22 22"><path d="M4 2l16 9-16 9z" fill="#d9c3fb"/></svg>
    Watch Our Vedio
  </div>

  <p class="abs eyebrow about-text about-eyebrow">About The Agency</p>
  <h2 class="abs about-text about-title">We Create Websites That Inspire</h2>
  <p class="abs about-text about-copy" style="top:1362px;width:290px">We are a collaborative team of word nerds, choreographers of shapes &amp; ideas, ambassadors of data, content warriors and inspirational conversationalists ready to help you no matter where you are in your journey.</p>
  <p class="abs about-text about-copy" style="top:1456px;width:290px">We have a deep understanding of what it takes to grow a business and we collaborate with you every step of the way from strategy to implementation and beyond.</p>

  <div class="abs feature" style="left:611px;top:1545px">
    <h3>Proven Process</h3>
    <svg width="32" height="32" viewBox="0 0 32 32" fill="none" stroke="#a55ff2" stroke-width="1.5"><rect x="3" y="3" width="26" height="26" rx="2"/><path d="M8 12l3 3 5-6M8 22h16M19 12h5"/></svg>
    <p>We have carefully crafted each step in our process for successful outcomes.</p>
  </div>
  <div class="abs feature" style="left:850px;top:1545px">
    <h3>Connection</h3>
    <svg width="32" height="32" viewBox="0 0 32 32" fill="none" stroke="#a55ff2" stroke-width="1.5"><circle cx="16" cy="16" r="12"/><path d="M10 16h12M16 10v12"/></svg>
    <p>We take the time to truly listen and understand your audience and business needs.</p>
  </div>
  <div class="abs feature" style="left:611px;top:1645px">
    <h3>Exceeding Your Goals</h3>
    <svg width="32" height="32" viewBox="0 0 32 32" fill="none" stroke="#a55ff2" stroke-width="1.5"><rect x="3" y="5" width="26" height="20" rx="2"/><path d="M8 20l5-6 4 3 7-8"/></svg>
    <p>We develop actionable strategies for success based on your unique goals.</p>
  </div>
</section>

<section class="abs testimonials">
  <h2>What Our Client Say</h2>
  <p class="lead">Lorem Ipsum is simply dummy text of the printing and typesetting industry. Lorem Ipsum has been the industry's standard dummy text ever since the 1500s, when an unknown printer took a galley of type and scrambled it to make a type specimen book.</p>

  <article class="abs quote-card outline" style="left:125px">
    <h3>Rowan Ellis</h3>
    <p>Lorem Ipsum is simply dummy text of the printing and typesetting industry. Lorem Ipsum has been the industry's standard dummy text ever since the 1500s, when an unknown printer took a galley of type and scrambled it to make a type specimen book.</p>
    <div class="quote-badge"><svg width="20" height="16" viewBox="0 0 20 16" fill="#a55ff2"><path d="M0 16V9C0 4 2 1 7 0l1 2C5 3 4 5 4 7h4v9zM11 16V9c0-5 2-8 7-9l1 2c-3 1-4 3-4 5h4v9z"/></svg></div>
  </article>
  <article class="abs quote-card filled" style="left:447px">
    <h3>Tessa Marlow</h3>
    <p>Lorem Ipsum is simply dummy text of the printing and typesetting industry. Lorem Ipsum has been the industry's standard dummy text ever since the 1500s, when an unknown printer took a galley of type and scrambled it to make a type specimen book.</p>
    <div class="quote-badge"><svg width="20" height="16" viewBox="0 0 20 16" fill="#a55ff2"><path d="M0 16V9C0 4 2 1 7 0l1 2C5 3 4 5 4 7h4v9zM11 16V9c0-5 2-8 7-9l1 2c-3 1-4 3-4 5h4v9z"/></svg></div>
  </article>
  <article class="abs quote-card filled" style="left:772px">
    <h3>Owen Hartley</h3>
    <p>Lorem Ipsum is simply dummy text of the printing and typesetting industry. Lorem Ipsum has been the industry's standard dummy text ever since the 1500s, when an unknown printer took a galley of type and scrambled it to make a type specimen book.</p>
    <div class="quote-badge"><svg width="20" height="16" viewBox="0 0 20 16" fill="#a55ff2"><path d="M0 16V9C0 4 2 1 7 0l1 2C5 3 4 5 4 7h4v9zM11 16V9c0-5 2-8 7-9l1 2c-3 1-4 3-4 5h4v9z"/></svg></div>
  </article>
</section>

<section class="cta">
  <h2 class="abs cta-title">Have Any Projects In<br>Mind?<br>Get In Touch With Us!</h2>
  <div class="abs cta-btn"><span class="label">Let's Talk</span><span class="arrow-line"></span></div>
</section>

<footer class="abs site-footer">
  <div class="abs brand footer-brand"><span class="dot"></span>Lumora Works</div>
  <div class="abs social" aria-label="Social links"><span></span><span></span><span></span><span></span></div>
  <div class="abs footer-rule"></div>
  <p class="abs footer-kicker">Let's start working together</p>
  <p class="abs footer-email">Hello@Lumoraworks.Example</p>
  <p class="abs copyright">© Copyright 2024 by <b>Lumora Works</b></p>
  <ul class="abs footer-links" style="left:817px"><li>Home</li><li>About Us</li><li>Services</li><li>Blogs</li><li>Contact</li></ul>
  <ul class="abs footer-links" style="left:922px"><li>Privacy</li><li>Terms</li><li>Disclaimer.</li></ul>
</footer>

</body>
</html>
```